Need a design for Office wall, Pull up banner and brochure.

Hi there, We are looking for a design for our Mission, Vision and Values. We need it for our wall design, our pull up banner, and for our brochure. Full instructions have been provided in the Instructions png file submitted. Please let me know.

Our brand colours are:

Brand colours:
#0070BA
#000A3F
#6D6E71

Font styles to use
Other font styles liked:
• FF Meta Georgian Book

Colors

Designer to choose colors to be used in the design.

```html
<!DOCTYPE html>
<html lang="en">
<head>
<meta charset="utf-8">
<title>Ashcombe Reid – Mission, Values &amp; Vision</title>
<link href="https://fonts.googleapis.com/css2?family=Fira+Sans:wght@400;500;700&family=Fira+Sans+Condensed:wght@500;700&display=swap" rel="stylesheet">
<style>
  :root {
    --brand-blue: #0070BA;
    --brand-navy: #000A3F;
    --brand-grey: #6D6E71;
    --logo-ink: #33366b;
    --stage: #d5d6d8;
    --paper: #ffffff;
    --paper-tint: #f1f2f3;
  }
  html, body {
    margin: 0;
    padding: 0;
    width: 727px;
    height: 1200px;
    overflow: hidden;
    background: var(--stage);
  }
  .artwork { display: block; width: 727px; height: 1200px; }
  .brand-name { font-family: "Fira Sans", sans-serif; font-weight: 400; fill: var(--logo-ink); letter-spacing: 0.5px; }
  .brand-tagline { font-family: "Fira Sans", sans-serif; font-weight: 400; fill: var(--brand-grey); letter-spacing: 0.4px; }
  .brand-incorporating { font-family: "Fira Sans", sans-serif; font-weight: 500; fill: var(--logo-ink); letter-spacing: 0.8px; }
  .section-title { font-family: "Fira Sans Condensed", sans-serif; font-weight: 700; letter-spacing: 0.3px; }
  .section-body { font-family: "Fira Sans", sans-serif; font-weight: 400; }
  .value-label { font-family: "Fira Sans", sans-serif; font-weight: 500; letter-spacing: 0.2px; }
  .on-dark { fill: #ffffff; }
  .ink-blue { fill: var(--brand-blue); }
  .ink-grey { fill: var(--brand-grey); }
  .ink-navy { fill: var(--brand-navy); }
  .ink-body { fill: #1d1f2c; }
  .scallop { fill: none; stroke-width: 3.2; stroke-dasharray: 1.6 1.9; stroke-linecap: round; }
  .rule { fill: none; stroke-width: 1.6; }
</style>
</head>
<body>
<svg class="artwork" viewBox="0 0 727 1200" xmlns="http://www.w3.org/2000/svg">
  <defs>
    <linearGradient id="paper-sheen" x1="0" y1="0" x2="1" y2="1">
      <stop offset="0" stop-color="var(--paper-tint)"/>
      <stop offset="0.5" stop-color="var(--paper)"/>
      <stop offset="1" stop-color="var(--paper-tint)"/>
    </linearGradient>
    <linearGradient id="fold-shade" x1="0" y1="0" x2="0" y2="1">
      <stop offset="0" stop-color="#000" stop-opacity="0.28"/>
      <stop offset="1" stop-color="#000" stop-opacity="0"/>
    </linearGradient>
    <clipPath id="clip-mission"><circle cx="214" cy="306" r="83"/></clipPath>
    <clipPath id="clip-values"><circle cx="361" cy="306" r="83"/></clipPath>
    <clipPath id="clip-vision"><circle cx="512" cy="306" r="83"/></clipPath>

    <symbol id="icon-target" viewBox="0 0 40 40">
      <g fill="none" stroke="currentColor" stroke-width="2.6" stroke-linecap="round">
        <circle cx="19" cy="21" r="16"/>
        <circle cx="19" cy="21" r="10.5"/>
        <circle cx="19" cy="21" r="5"/>
        <line x1="19" y1="21" x2="33" y2="7"/>
        <polyline points="29,5 33,7 35,11"/>
      </g>
    </symbol>
    <symbol id="icon-eye" viewBox="0 0 40 40">
      <g fill="none" stroke="currentColor" stroke-width="2.6" stroke-linecap="round">
        <path d="M3 22 Q20 7 37 22 Q20 37 3 22 Z"/>
        <circle cx="19" cy="22" r="5.5"/>
        <line x1="23" y1="26" x2="32" y2="35" stroke-width="4"/>
        <line x1="20" y1="4" x2="20" y2="8"/>
        <line x1="11" y1="6" x2="13" y2="10"/>
        <line x1="29" y1="6" x2="27" y2="10"/>
        <line x1="4" y1="10" x2="7" y2="13"/>
        <line x1="36" y1="10" x2="33" y2="13"/>
      </g>
    </symbol>
    <symbol id="icon-care" viewBox="0 0 40 40">
      <path fill="currentColor" d="M20 15 C20 10 13 9 12.5 14.5 C12 19 20 24 20 24 C20 24 28 19 27.5 14.5 C27 9 20 10 20 15 Z"/>
      <path fill="none" stroke="currentColor" stroke-width="3" stroke-linecap="round" stroke-linejoin="round"
            d="M6 12 L6 25 Q6 31 14 33 L14 38 M34 12 L34 25 Q34 31 26 33 L26 38"/>
    </symbol>
  </defs>

  <!-- ===== Wall piece (landscape) ===== -->
  <g class="wall-piece">
    <rect x="104" y="73" width="520" height="367" fill="url(#paper-sheen)"/>

    <g class="brand-lockup">
      <text class="brand-name" x="472" y="134" text-anchor="end" font-size="21">Ashcombe Reid</text>
      <text class="brand-tagline" x="472" y="149" text-anchor="end" font-size="11.5">Accountants &amp; Business Advisors</text>
      <text class="brand-incorporating" x="472" y="164" text-anchor="end" font-size="7.6">INCORPORATING PETER M LAWSON</text>
    </g>

    <!-- disc shapes -->
    <g class="disc disc-mission">
      <circle cx="214" cy="306" r="95" fill="var(--paper)"/>
      <circle class="scallop" cx="214" cy="306" r="94" stroke="var(--brand-blue)"/>
      <circle class="rule" cx="214" cy="306" r="91" stroke="var(--brand-blue)"/>
      <circle cx="214" cy="306" r="83" fill="var(--brand-blue)"/>
      <rect x="122" y="306" width="190" height="7" fill="url(#fold-shade)" clip-path="url(#clip-mission)"/>
    </g>
    <g class="disc disc-vision">
      <circle cx="512" cy="306" r="95" fill="var(--paper)"/>
      <circle class="scallop" cx="512" cy="306" r="94" stroke="var(--brand-navy)"/>
      <circle class="rule" cx="512" cy="306" r="91" stroke="var(--brand-navy)"/>
      <circle cx="512" cy="306" r="83" fill="var(--brand-navy)"/>
      <rect x="420" y="306" width="190" height="7" fill="url(#fold-shade)" clip-path="url(#clip-vision)"/>
    </g>
    <g class="disc disc-values">
      <circle cx="361" cy="306" r="95" fill="var(--paper)"/>
      <circle class="scallop" cx="361" cy="306" r="94" stroke="var(--brand-grey)"/>
      <circle class="rule" cx="361" cy="306" r="91" stroke="var(--brand-grey)"/>
      <circle cx="361" cy="306" r="83" fill="var(--brand-grey)"/>
      <rect x="270" y="306" width="190" height="7" fill="url(#fold-shade)" clip-path="url(#clip-values)"/>
    </g>

    <!-- disc content -->
    <g class="disc-content content-mission">
      <text class="section-title on-dark" x="212" y="255" text-anchor="middle" font-size="13.5">MISSION</text>
      <g class="section-body on-dark" font-size="5.4" text-anchor="middle">
        <text x="212" y="267">Our Mission at Ashcombe Reid to provide</text>
        <text x="212" y="275">quality business services through</text>
        <text x="212" y="283">advice &amp; guidance together with</text>
        <text x="212" y="290.5">building long-term business</text>
        <text x="212" y="298">relationships</text>
      </g>
      <use href="#icon-target" x="189" y="320" width="46" height="46" style="color:#fff"/>
    </g>

    <g class="disc-content content-values">
      <use href="#icon-care" x="306" y="249" width="38" height="38" style="color:#fff"/>
      <text class="section-title on-dark" x="349" y="262" text-anchor="start" font-size="13.5">VALUES</text>
      <g class="section-body on-dark" font-size="5.6">
        <text x="349" y="271">Integrity &amp; Professionalism</text>
        <text x="349" y="279">Trust &amp; Respect, Efficency</text>
        <text x="349" y="286.5">&amp; Commitment</text>
      </g>
      <g class="value-list" fill="none" stroke="#fff" stroke-width="0.7">
        <circle cx="312" cy="320" r="4.5"/><circle cx="368" cy="320" r="4.5"/>
        <circle cx="312" cy="338" r="4.5"/><circle cx="368" cy="338" r="4.5"/>
        <circle cx="312" cy="355" r="4.5"/><circle cx="368" cy="355" r="4.5"/>
        <line x1="355.5" y1="316" x2="355.5" y2="323"/>
        <line x1="355.5" y1="334" x2="355.5" y2="341"/>
        <line x1="355.5" y1="351" x2="355.5" y2="358"/>
      </g>
      <g class="value-label on-dark" font-size="4.8">
        <text x="320" y="322">INTEGRITY</text><text x="376" y="322">TRUST</text>
        <text x="320" y="340">EFFICIENCY</text><text x="376" y="340">PROFESSIONALISM</text>
        <text x="320" y="357">RESPECT</text><text x="376" y="357">COMMITMENT</text>
      </g>
    </g>

    <g class="disc-content content-vision">
      <text class="section-title on-dark" x="514" y="255" text-anchor="middle" font-size="13.5">VISION</text>
      <g class="section-body on-dark" font-size="5.4" text-anchor="middle">
        <text x="516" y="266">To be the leading accounting firm in</text>
        <text x="516" y="274">our community, known for providing</text>
        <text x="516" y="281.5">businesses &amp; individuals with</text>
        <text x="516" y="289">innovative &amp; expert support enabling</text>
        <text x="516" y="297">our clients to achieve Financial success</text>
      </g>
      <use href="#icon-eye" x="488" y="315" width="54" height="54" style="color:#fff"/>
    </g>
  </g>

  <!-- ===== Pull-up banner (portrait) ===== -->
  <g class="banner-piece">
    <rect x="240" y="509" width="247" height="619" fill="url(#paper-sheen)"/>

    <g class="brand-lockup">
      <text class="brand-name" x="456" y="561" text-anchor="end" font-size="18">Ashcombe Reid</text>
      <text class="brand-tagline" x="456" y="574" text-anchor="end" font-size="10">Accountants &amp; Business Advisors</text>
      <text class="brand-incorporating" x="456" y="587" text-anchor="end" font-size="6.8">INCORPORATING PETER M LAWSON</text>
    </g>

    <!-- Mission -->
    <g class="stack stack-mission">
      <path d="M363.5 613 A88 88 0 0 1 363.5 789 Z" fill="var(--brand-blue)"/>
      <circle cx="365" cy="701" r="71" fill="var(--paper)"/>
      <circle class="scallop" cx="365" cy="701" r="67" stroke="var(--brand-blue)" stroke-width="2.6"/>
      <circle class="rule" cx="365" cy="701" r="63.5" stroke="var(--brand-blue)" stroke-width="1.2"/>
      <circle cx="294" cy="701" r="20" fill="var(--paper)" stroke="var(--brand-blue)" stroke-width="2.4"/>
      <use href="#icon-target" x="279" y="686" width="30" height="30" style="color:var(--brand-blue)"/>
      <text class="section-title ink-blue" x="368" y="677" text-anchor="middle" font-size="12.5">MISSION</text>
      <g class="section-body ink-body" font-size="5.6" text-anchor="middle">
        <text x="368" y="689">Our Mission at Ashcombe Reid to provide</text>
        <text x="368" y="696">quality business services through</text>
        <text x="368" y="703">advice &amp; guidance together with</text>
        <text x="368" y="710">building long-term business</text>
        <text x="368" y="717">relationships</text>
      </g>
      <g fill="var(--brand-blue)">
        <circle cx="355" cy="737" r="0.9"/><circle cx="359.5" cy="737" r="0.9"/><circle cx="364" cy="737" r="0.9"/><circle cx="368.5" cy="737" r="0.9"/><circle cx="373" cy="737" r="0.9"/>
      </g>
    </g>

    <!-- Values -->
    <g class="stack stack-values">
      <path d="M363.5 773 A87 87 0 0 0 363.5 947 Z" fill="var(--brand-grey)"/>
      <circle cx="363.5" cy="860" r="71" fill="var(--paper)"/>
      <circle class="scallop" cx="363.5" cy="860" r="67" stroke="var(--brand-grey)" stroke-width="2.6"/>
      <circle class="rule" cx="363.5" cy="860" r="63.5" stroke="var(--brand-grey)" stroke-width="1.2"/>
      <circle cx="435" cy="860" r="20" fill="var(--paper)" stroke="var(--brand-grey)" stroke-width="2.4"/>
      <use href="#icon-care" x="421" y="846" width="28" height="28" style="color:var(--brand-grey)"/>
      <text class="section-title ink-grey" x="365" y="825" text-anchor="middle" font-size="12.5">VALUES</text>
      <g class="section-body ink-body" font-size="5.6" text-anchor="middle">
        <text x="365" y="835">Integrity and Professionalism Trust &amp;</text>
        <text x="365" y="842">Respect, Efficency &amp; Commitment</text>
      </g>
      <g fill="none" stroke="var(--brand-grey)" stroke-width="0.6">
        <circle cx="337" cy="852" r="4"/><circle cx="386" cy="852" r="4"/>
        <circle cx="337" cy="872" r="4"/><circle cx="386" cy="872" r="4"/>
        <circle cx="337" cy="892" r="4"/><circle cx="386" cy="892" r="4"/>
        <line x1="360" y1="849" x2="360" y2="855"/>
        <line x1="360" y1="869" x2="360" y2="875"/>
        <line x1="360" y1="889" x2="360" y2="895"/>
      </g>
      <g class="value-label ink-body" font-size="4.6" text-anchor="middle">
        <text x="337" y="863">INTEGRITY</text><text x="386" y="863">TRUST</text>
        <text x="337" y="883">EFFICIENCY</text><text x="386" y="883">PROFESSIONALISM</text>
        <text x="337" y="903">RESPECT</text><text x="386" y="903">COMMITMENT</text>
      </g>
    </g>

    <!-- Vision -->
    <g class="stack stack-vision">
      <path d="M363.5 933 A88 88 0 0 1 363.5 1109 Z" fill="var(--brand-navy)"/>
      <circle cx="365" cy="1021" r="71" fill="var(--paper)"/>
      <circle class="scallop" cx="365" cy="1021" r="67" stroke="var(--brand-navy)" stroke-width="2.6"/>
      <circle class="rule" cx="365" cy="1021" r="63.5" stroke="var(--brand-navy)" stroke-width="1.2"/>
      <circle cx="292" cy="1022" r="20" fill="var(--paper)" stroke="var(--brand-navy)" stroke-width="2.4"/>
      <use href="#icon-eye" x="276" y="1006" width="32" height="32" style="color:var(--brand-navy)"/>
      <text class="section-title ink-navy" x="366" y="999" text-anchor="middle" font-size="12.5">VISION</text>
      <g class="section-body ink-body" font-size="5.6" text-anchor="middle">
        <text x="366" y="1011">To be the leading accounting firm in</text>
        <text x="366" y="1018">our community, known for providing</text>
        <text x="366" y="1025">businesses &amp; individuals with</text>
        <text x="366" y="1032">innovative &amp; expert support enabling</text>
        <text x="366" y="1039">our clients to achieve Financial success</text>
      </g>
      <g fill="var(--brand-navy)">
        <circle cx="355" cy="1054" r="0.9"/><circle cx="359.5" cy="1054" r="0.9"/><circle cx="364" cy="1054" r="0.9"/><circle cx="368.5" cy="1054" r="0.9"/><circle cx="373" cy="1054" r="0.9"/>
      </g>
    </g>
  </g>
</svg>
</body>
</html>
```